web site update

I want to get a better website for a small high end remodeling and construction company
I currently have a web site but you will find that it is not good.
www.pelbrookhaven.com
We are a high end construction / remodeling company that has been in business since 2003. We primarily work in the mid peninsula of the bay area. Most of our clientele are very educated captains of industry. This group is still the target client.
I had my logo designed by Vellum Forge a few years ago and I do like it, I like the orange and black or orange a blue. I don’t have a lot of content on hand as far as professional photographs.
Number of pages not sure and are open to: design pages vs full function website
I think what I am after is a web presence that will seal the deal as we are getting high referrals from past clients.
Construction
1 page

```html
<!DOCTYPE html>
<html lang="en">
<head>
<meta charset="utf-8">
<title>Pelbrook Haven Property Management</title>
<link href="https://fonts.googleapis.com/css2?family=Lato:ital,wght@0,400;0,700;0,900;1,700&display=swap" rel="stylesheet">
<style>
:root{
  --orange:#f26d21;
  --orange-soft:#f9a262;
  --black:#000;
  --ink:#333;
  --text:#4a4a4a;
  --white:#fff;
  --rule:#d9d9d9;
}
*{box-sizing:border-box;margin:0;padding:0}
html,body{width:1200px;height:2341px;overflow:hidden;background:var(--white)}
body{font-family:'Lato',sans-serif;color:var(--ink);position:relative}

.site-header{position:absolute;left:0;top:0;width:1200px;height:145px}
.brand{position:absolute;left:76px;top:30px;display:flex;align-items:center;gap:18px}
.brand-mark{width:72px;height:72px;background:var(--orange)}
.brand-name{font-family:'Lato',sans-serif;font-weight:900;font-size:40px;line-height:1.05;color:var(--orange);text-transform:uppercase;letter-spacing:1px}
.contact{position:absolute;right:86px;font-size:16px;font-style:italic;font-weight:700;color:var(--orange);display:flex;align-items:center;gap:12px}
.contact svg{flex:none}
.contact-phone{top:40px}
.contact-mail{top:96px}

.main-nav{position:absolute;left:0;top:146px;width:1200px;height:44px;background:var(--black)}
.main-nav ul{list-style:none;display:flex;padding-left:76px;height:100%}
.main-nav li{color:var(--white);font-size:14.5px;height:100%;display:flex;align-items:center;padding:0 9px}
.main-nav li.active{background:var(--orange);padding:0 21px}

.hero{position:absolute;left:76px;top:190px;width:1051px;height:398px;background:linear-gradient(180deg,#e9a27a 0%,#d98a5e 45%,#c9794e 100%)}
.hero-band{position:absolute;left:0;bottom:0;width:100%;height:40px;background:var(--orange);opacity:.9}
.hero-title{position:absolute;left:0;width:100%;top:302px;text-align:center;color:var(--white);font-size:40px;font-weight:700;font-style:italic}
.hero-sub{position:absolute;left:0;width:100%;top:368px;text-align:center;color:var(--white);font-size:18px;letter-spacing:1px}

.welcome{position:absolute;left:0;top:642px;width:1200px;text-align:center}
.welcome h1{font-weight:400;font-size:30px;color:var(--ink);line-height:1.2}
.welcome h2{font-weight:700;font-size:25px;color:#444;line-height:1.3;margin-top:2px}

.intro-col{position:absolute;top:764px;font-size:13px;line-height:16.6px;color:var(--text);text-align:center}
.intro-col strong{color:#111}
.intro-a{left:76px;width:392px}
.intro-b{left:514px;width:282px}
.intro-photo{position:absolute;left:835px;top:772px;width:290px;height:188px;background:linear-gradient(135deg,#4f6b4a 0%,#8a7560 50%,#d98a3c 100%)}

.divider{position:absolute;left:76px;top:1037px;width:1051px;height:2px;background:var(--rule)}

.services{position:absolute;left:76px;top:1116px;width:1051px;display:grid;grid-template-columns:repeat(3,320px);column-gap:45px;row-gap:42px}
.card{height:501px;background:var(--orange-soft);color:var(--white);position:relative}
.card-photo{height:242px}
.card h3{font-size:17px;font-weight:700;margin:30px 32px 0}
.card p{font-size:12.5px;line-height:20px;margin:14px 32px 0}
.card .more{position:absolute;left:32px;bottom:52px;font-size:11.5px;font-weight:700;display:flex;align-items:center;gap:6px}
.ph-towers{background:linear-gradient(180deg,#9bbad6,#5c5c5c)}
.ph-builder{background:linear-gradient(180deg,#6e97c4,#7a6f64)}
.ph-plans{background:linear-gradient(180deg,#c8a27a,#8a6a4a)}
.ph-site{background:linear-gradient(180deg,#b9b9b9,#6b6b6b)}
.ph-couple{background:linear-gradient(180deg,#d7c3a6,#5e86b4)}
.ph-meeting{background:linear-gradient(180deg,#a9c3d9,#3a3f4a)}

.site-footer{position:absolute;left:0;top:2228px;width:1200px;height:113px;background:var(--black);color:var(--white);text-align:center}
.footer-line{position:absolute;left:0;top:39px;width:100%;display:flex;justify-content:center;align-items:center;gap:14px;font-size:12.5px}
.footer-line b{font-weight:700}
.footer-line span{display:flex;align-items:center;gap:5px}
.copyright{position:absolute;left:0;top:76px;width:100%;font-size:9.5px}
</style>
</head>
<body>

<header class="site-header">
  <div class="brand">
    <div class="brand-mark"></div>
    <div class="brand-name">Pelbrook Haven<br>Remodeling</div>
  </div>
  <div class="contact contact-phone">
    <svg width="26" height="24" viewBox="0 0 24 24"><path d="M6.6 10.8a15 15 0 0 0 6.6 6.6l2.2-2.2a1 1 0 0 1 1-.25 11.4 11.4 0 0 0 3.6.57 1 1 0 0 1 1 1V20a1 1 0 0 1-1 1A17 17 0 0 1 3 4a1 1 0 0 1 1-1h3.5a1 1 0 0 1 1 1c0 1.25.2 2.45.57 3.57a1 1 0 0 1-.25 1z" fill="#000"/></svg>
    415 - 555 - 0142
  </div>
  <div class="contact contact-mail">
    <svg width="32" height="24" viewBox="0 0 32 24"><rect x="1.5" y="1.5" width="29" height="21" fill="none" stroke="#000" stroke-width="2.5"/><path d="M2 3l14 11 14-11" fill="none" stroke="#000" stroke-width="2.5"/></svg>
    info@pelbrookhaven.com
  </div>
</header>

<nav class="main-nav">
  <ul>
    <li class="active">Home</li>
    <li>Property Managemnt</li>
    <li style="padding-left:22px">Residential Reas Estate</li>
    <li>Commercial Real Estate</li>
    <li>Construction Managemnt</li>
    <li style="padding-left:14px">Building Maintenance</li>
    <li>Repairs</li>
    <li>Contact</li>
  </ul>
</nav>

<section class="hero" role="img" aria-label="Couple standing in front of a house with an orange facade">
  <div class="hero-band"></div>
  <div class="hero-title">Pelbrook Haven Property Management</div>
  <div class="hero-sub">is a full - service real estate management company</div>
</section>

<section class="welcome">
  <h1>WELCOME</h1>
  <h2>Pelbrook Haven Property Managemnt</h2>
</section>

<p class="intro-col intro-a"><strong>Lorem ipsum dolor sit amet, consectetur adipisicing elit, sed do eiusmod tempor incididunt ut labore et dolore magna aliqua.</strong> Ut enim ad minim veniam, quis nostrud exercitation ullamco laboris nisi ut aliquip ex ea commodo consequat. Duis aute irure dolor in reprehenderit in voluptate velit esse cillum dolore eu fugiat nulla pariatur. Excepteur sint occaecat cupidatat non proident, sunt in culpa qui officia deserunt mollit anim id est laborum. Sed ut perspiciatis unde omnis iste natus error sit voluptatem accusantium doloremque laudantium, totam rem aperiam, eaque ipsa quae ab illo inventore veritatis et quasi architecto beatae vitae dicta sunt explicabo. Nemo enim ipsam voluptatem quia voluptas sit</p>

<p class="intro-col intro-b"><strong>Lorem ipsum dolor sit amet,</strong> consectetur adipisicing elit, sed do eiusmod tempor incididunt ut labore et dolore magna aliqua. Ut enim ad minim veniam, quis nostrud exercitation ullamco laboris nisi ut aliquip ex ea commodo consequat. Duis aute irure dolor in reprehenderit in voluptate velit esse cillum dolore eu fugiat nulla pariatur. Excepteur sint occaecat cupidatat non proident, sunt in culpa qui officia deserunt mollit anim id est laborum. Sed ut</p>

<div class="intro-photo" role="img" aria-label="Modern home with glass walls and warm interior lighting at dusk"></div>

<div class="divider"></div>

<section class="services">
  <article class="card">
    <div class="card-photo ph-towers" role="img" aria-label="High-rise towers under construction with a crane"></div>
    <h3>Commercila Real Estate</h3>
    <p>We are the 4/7, 365 day single source provider for all your commercial cleaning service needs. Whether you need a one time service call or an ongoing maintenance program, we can cater</p>
    <div class="more">MORE <svg width="20" height="8" viewBox="0 0 20 8"><path d="M0 4h18M14 1l4 3-4 3" fill="none" stroke="#fff" stroke-width="1.3"/></svg></div>
  </article>
  <article class="card">
    <div class="card-photo ph-builder" role="img" aria-label="Builder measuring a pipe in front of a house under construction"></div>
    <h3>Residentiala Real Estate</h3>
    <p>We are the 4/7, 365 day single source provider for all your commercial cleaning service needs. Whether you need a one time service call or an ongoing maintenance program, we can cater</p>
    <div class="more">MORE <svg width="20" height="8" viewBox="0 0 20 8"><path d="M0 4h18M14 1l4 3-4 3" fill="none" stroke="#fff" stroke-width="1.3"/></svg></div>
  </article>
  <article class="card">
    <div class="card-photo ph-plans" role="img" aria-label="Two builders in hard hats reviewing plans inside a timber frame"></div>
    <h3>Evaluate Property</h3>
    <p>We are the 4/7, 365 day single source provider for all your commercial cleaning service needs. Whether you need a one time service call or an ongoing maintenance program, we can cater</p>
    <div class="more">MORE <svg width="20" height="8" viewBox="0 0 20 8"><path d="M0 4h18M14 1l4 3-4 3" fill="none" stroke="#fff" stroke-width="1.3"/></svg></div>
  </article>
  <article class="card">
    <div class="card-photo ph-site" role="img" aria-label="Engineers in hard hats looking at a building site"></div>
    <h3>Market Property</h3>
    <p>We are the 4/7, 365 day single source provider for all your commercial cleaning service needs. Whether you need a one time service call or an ongoing maintenance program, we can cater</p>
    <div class="more">MORE <svg width="20" height="8" viewBox="0 0 20 8"><path d="M0 4h18M14 1l4 3-4 3" fill="none" stroke="#fff" stroke-width="1.3"/></svg></div>
  </article>
  <article class="card">
    <div class="card-photo ph-couple" role="img" aria-label="Couple reading blueprints in front of a new house frame"></div>
    <h3>Tenant Screening</h3>
    <p>We are the 4/7, 365 day single source provider for all your commercial cleaning service needs. Whether you need a one time service call or an ongoing maintenance program, we can cater</p>
    <div class="more">MORE <svg width="20" height="8" viewBox="0 0 20 8"><path d="M0 4h18M14 1l4 3-4 3" fill="none" stroke="#fff" stroke-width="1.3"/></svg></div>
  </article>
  <article class="card">
    <div class="card-photo ph-meeting" role="img" aria-label="Three professionals meeting over a laptop outside office towers"></div>
    <h3>Property Maintenance</h3>
    <p>We are the 4/7, 365 day single source provider for all your commercial cleaning service needs. Whether you need a one time service call or an ongoing maintenance program, we can cater</p>
    <div class="more">MORE <svg width="20" height="8" viewBox="0 0 20 8"><path d="M0 4h18M14 1l4 3-4 3" fill="none" stroke="#fff" stroke-width="1.3"/></svg></div>
  </article>
</section>

<footer class="site-footer">
  <div class="footer-line">
    <span>Pelbrook Haven Property Managemtn, LLC | PO BOX 418 | Fairmont, CA | 94010</span>
    <span><svg width="18" height="14" viewBox="0 0 24 24"><path d="M6.6 10.8a15 15 0 0 0 6.6 6.6l2.2-2.2a1 1 0 0 1 1-.25 11.4 11.4 0 0 0 3.6.57 1 1 0 0 1 1 1V20a1 1 0 0 1-1 1A17 17 0 0 1 3 4a1 1 0 0 1 1-1h3.5a1 1 0 0 1 1 1c0 1.25.2 2.45.57 3.57a1 1 0 0 1-.25 1z" fill="#fff"/></svg><b>8005550199</b></span>
    <span><svg width="12" height="12" viewBox="0 0 12 12"><rect x="2" y="0.5" width="8" height="3" fill="#fff"/><rect x="0.5" y="4" width="11" height="5" fill="#fff"/><rect x="2.5" y="8" width="7" height="3.5" fill="#fff"/></svg><b>800.555.0177</b></span>
    <span><svg width="12" height="10" viewBox="0 0 12 10"><rect x="0.6" y="0.6" width="10.8" height="8.8" fill="none" stroke="#fff" stroke-width="1.2"/><path d="M1 1l5 4 5-4" fill="none" stroke="#fff" stroke-width="1.2"/></svg><b>info@pelbrookhaven.com</b></span>
  </div>
  <div class="copyright">Copyright @ 2016 pelbrookhaven.com . All right reserved.</div>
</footer>

</body>
</html>
```